PLOVEN Business Card

Coastal Build Additions and Refits. I need a business card designed for this new high end renovation business. I would like the logo centered on the back side with the ABN (37 915 402 176) on the bottom right hand corner.

I would like the following information placed on the other side along with some customized pattern or design.

Derek Collwood
Director
Phone: 1300 480 957
Fax: (02) 8145 9021
Website: www.plovenbuilders.com.au
Email: d.collwood@plovenbuilders.com.au
PO Box 87,
Kelvinbrook NSW 2069

(FB Logo) PLOVEN - Coastal Build Additions and Refits

The final design should communicate professionalism and trust.

Back side background colour: white
Front side: Undecided

```html
<!DOCTYPE html>
<html lang="en">
<head>
<meta charset="utf-8">
<title>PLOVEN Business Card</title>
<link rel="stylesheet" href="https://fonts.googleapis.com/css2?family=Open+Sans:wght@400;600;700&family=Cinzel:wght@400&display=swap">
<style>
  :root {
    --page: #e9ebee;
    --card: #ffffff;
    --navy: #1b3a6b;
    --blue: #1f6fb5;
    --blue-light: #2a9de0;
    --ink: #2b2b2b;
    --rule: #3a3a3a;
  }
  * { box-sizing: border-box; margin: 0; padding: 0; }
  html, body { width: 1200px; height: 1000px; overflow: hidden; }
  body {
    background: var(--page);
    font-family: "Open Sans", Arial, sans-serif;
    color: var(--ink);
    position: relative;
  }
  .card {
    position: absolute;
    left: 250px;
    width: 700px;
    height: 400px;
    background: var(--card);
    box-shadow: 0 6px 22px rgba(0,0,0,0.14);
    overflow: hidden;
  }
  .card--front { top: 60px; }
  .card--back { top: 540px; }

  .card__art { position: absolute; inset: 0; width: 700px; height: 400px; }

  /* Brand block */
  .brand { position: absolute; text-align: center; }
  .brand__name {
    font-family: "Open Sans", Arial, sans-serif;
    font-weight: 700;
    color: var(--navy);
    letter-spacing: 4px;
    line-height: 1;
  }
  .brand__tagline {
    display: flex;
    align-items: center;
    gap: 8px;
    font-family: "Cinzel", Georgia, serif;
    color: var(--blue);
    text-transform: uppercase;
    white-space: nowrap;
  }
  .brand__tagline::before,
  .brand__tagline::after {
    content: "";
    flex: 1;
    height: 1.5px;
    background: var(--blue);
  }

  .card--front .brand { left: 40px; top: 52px; width: 270px; }
  .card--front .brand__name { font-size: 48px; }
  .card--front .brand__tagline { font-size: 10px; margin-top: 10px; }

  .card--back .brand { left: 130px; top: 140px; width: 440px; }
  .card--back .brand__name { font-size: 78px; letter-spacing: 7px; }
  .card--back .brand__tagline { font-size: 16px; margin-top: 16px; gap: 12px; }

  /* Contact block */
  .contact { position: absolute; left: 368px; top: 72px; }
  .contact__name {
    font-size: 27px;
    font-weight: 700;
    color: var(--blue);
    letter-spacing: 1px;
    text-transform: uppercase;
    line-height: 1.1;
  }
  .contact__role { font-size: 16px; font-weight: 700; color: var(--ink); margin-bottom: 12px; }
  .contact__list { list-style: none; }
  .contact__item {
    display: flex;
    align-items: flex-start;
    gap: 10px;
    font-size: 16px;
    line-height: 1.55;
  }
  .contact__icon {
    flex: none;
    width: 17px;
    height: 17px;
    margin-top: 4px;
  }
  .contact__icon--none { visibility: hidden; }

  .website {
    position: absolute;
    left: 70px;
    top: 342px;
    font-size: 22px;
    color: #ffffff;
    letter-spacing: 0.5px;
    transform: rotate(2.6deg);
    transform-origin: left center;
  }

  .abn {
    position: absolute;
    right: 34px;
    bottom: 30px;
    font-size: 14px;
    letter-spacing: 0.5px;
    color: var(--ink);
  }
</style>
</head>
<body>

  <section class="card card--front" aria-label="Business card front">
    <svg class="card__art" viewBox="0 0 700 400" aria-hidden="true">
      <defs>
        <linearGradient id="bandFill" x1="0" y1="0" x2="1" y2="0">
          <stop offset="0" stop-color="#1a5fa3"/>
          <stop offset="1" stop-color="#2ba3e6"/>
        </linearGradient>
      </defs>
      <path d="M0,300 Q350,322 700,372 L700,400 L0,400 Z" fill="url(#bandFill)"/>
      <path d="M0,289 Q350,311 700,360" fill="none" stroke="var(--rule)" stroke-width="5"/>
      <line x1="30" y1="195" x2="340" y2="195" stroke="var(--rule)" stroke-width="2"/>
      <line x1="340" y1="72" x2="340" y2="195" stroke="var(--rule)" stroke-width="2"/>
    </svg>

    <div class="brand">
      <div class="brand__name">PLOVEN</div>
      <div class="brand__tagline">Coastal Build Additions &amp; Refits</div>
    </div>

    <div class="contact">
      <div class="contact__name">Derek Collwood</div>
      <div class="contact__role">Director</div>
      <ul class="contact__list">
        <li class="contact__item">
          <svg class="contact__icon" viewBox="0 0 17 17" aria-label="Phone"><rect width="17" height="17" rx="2" fill="var(--blue)"/><path d="M5 4h2l1 2.5-1.3 1a6 6 0 0 0 2.8 2.8l1-1.3 2.5 1v2a1 1 0 0 1-1 1A8 8 0 0 1 4 5a1 1 0 0 1 1-1z" fill="#fff"/></svg>
          <span>1300 480 957</span>
        </li>
        <li class="contact__item">
          <svg class="contact__icon" viewBox="0 0 17 17" aria-label="Fax"><rect width="17" height="17" rx="2" fill="var(--blue)"/><rect x="5" y="3.5" width="7" height="4" fill="#fff"/><rect x="3.5" y="7.5" width="10" height="5" rx="1" fill="#fff"/><rect x="5.5" y="11" width="6" height="2.5" fill="var(--blue)"/></svg>
          <span>(02) 8145 9021</span>
        </li>
        <li class="contact__item">
          <svg class="contact__icon" viewBox="0 0 17 17" aria-label="Email"><rect width="17" height="17" rx="2" fill="var(--blue)"/><rect x="3.5" y="5" width="10" height="7" fill="#fff"/><path d="M3.5 5l5 4 5-4" fill="none" stroke="var(--blue)" stroke-width="1.2"/></svg>
          <span>d.collwood@plovenbuilders.com.au</span>
        </li>
        <li class="contact__item">
          <svg class="contact__icon" viewBox="0 0 17 17" aria-label="Address"><rect width="17" height="17" rx="2" fill="var(--blue)"/><path d="M8.5 3a3.5 3.5 0 0 1 3.5 3.5c0 2.6-3.5 7-3.5 7S5 9.1 5 6.5A3.5 3.5 0 0 1 8.5 3z" fill="#fff"/><circle cx="8.5" cy="6.5" r="1.3" fill="var(--blue)"/></svg>
          <span>PO Box 87</span>
        </li>
        <li class="contact__item">
          <span class="contact__icon contact__icon--none"></span>
          <span>Kelvinbrook NSW 2069</span>
        </li>
      </ul>
    </div>

    <div class="website">www.plovenbuilders.com.au</div>
  </section>

  <section class="card card--back" aria-label="Business card back">
    <div class="brand">
      <div class="brand__name">PLOVEN</div>
      <div class="brand__tagline">Coastal Build Additions &amp; Refits</div>
    </div>
    <div class="abn">ABN (37 915 402 176)</div>
  </section>

</body>
</html>
```